Flyer für Therapie- und Gesundheitsdienstleister
Zielgruppe
Therapie- und Gesundheitsdienstleister im Bereich Physiotherapie, Podologie, Prävention und betriebliche Gesundheitsförderung. Für dieses Projekt möchten wir einen Flyer erstellen lassen für die Bewerbung der betrieblichen Gesundheitsförderungen in bzw. für Firmen
Aufgabenstellung
Klare Strukturen, nicht verspielt, DINA4 oder DINA5; leicht medizinischer Touch, evntuell Stockfotos integrieren, edel und hochwertiges Design

```html
<!DOCTYPE html>
<html lang="de">
<head>
<meta charset="utf-8">
<title>Betriebliche Gesundheitsförderung – Flyer</title>
<link rel="stylesheet" href="https://fonts.googleapis.com/css2?family=Montserrat:wght@300;400;600&family=Open+Sans:wght@700&display=swap">
<style>
  :root {
    --panel-grey: #c9ced6;
    --band-green: #cfe6cc;
    --heading: #4b4b4d;
    --body: #59595e;
    --navy: #2a2c4d;
    --paper: #fbfbfa;
  }
  * { margin: 0; padding: 0; box-sizing: border-box; }
  html, body { width: 1200px; height: 848px; overflow: hidden; background: #fff; }
  .flyer { position: relative; width: 1200px; height: 848px; font-family: "Montserrat", sans-serif; color: var(--body); }

  .column { position: absolute; top: 0; height: 848px; }
  .column--employer { left: 0; width: 396px; background: var(--panel-grey); }
  .column--analysis { left: 396px; width: 404px; background: var(--paper); }
  .column--programs { left: 800px; width: 400px; background: var(--panel-grey); }

  .title-band { position: absolute; left: 0; top: 32px; width: 1200px; height: 127px; background: var(--band-green); }
  .section-title {
    position: absolute; top: 32px; height: 127px;
    display: flex; align-items: center; justify-content: center; text-align: center;
    font-family: "Open Sans", sans-serif; font-weight: 700; font-size: 37px; line-height: 34px;
    color: var(--heading); letter-spacing: -0.2px;
  }
  .section-title--employer { left: 0; width: 420px; padding-top: 8px; }
  .section-title--analysis { left: 396px; width: 404px; padding-bottom: 6px; }
  .section-title--programs { left: 800px; width: 420px; padding-top: 8px; }

  .employer-text {
    position: absolute; left: 30px; top: 173px; width: 328px;
    font-size: 12.4px; font-weight: 300; line-height: 18.2px; text-align: justify; color: var(--body);
  }
  .employer-text p { margin-bottom: 18.2px; }
  .employer-text p.tight { margin-bottom: 0; }
  .employer-text strong { font-weight: 600; color: #3f3f44; }

  .analysis-text {
    position: absolute; left: 448px; top: 187px; width: 284px;
    font-size: 13.8px; font-weight: 300; line-height: 20.4px; text-align: justify; color: var(--body);
  }
  .analysis-text p { margin-bottom: 13px; }
  .analysis-text p.gap { margin-top: 26px; }

  .program-box {
    position: absolute; left: 816px; top: 176px; width: 369px; height: 433px;
    border: 2px solid var(--navy); border-radius: 3px;
  }
  .program { position: absolute; width: 180px; text-align: center; }
  .program__number {
    display: flex; align-items: center; justify-content: center;
    width: 44px; height: 44px; margin: 0 auto; border: 2px solid var(--navy); border-radius: 50%;
    font-size: 22px; font-weight: 300; color: var(--navy);
  }
  .program__label { position: absolute; left: 0; width: 180px; font-size: 14.2px; font-weight: 300; line-height: 18px; color: var(--body); }

  .photo { position: absolute; top: 651px; height: 197px; }
  .photo--group-class { left: 410px; width: 390px; background: linear-gradient(100deg, #e9d2c4 0%, #dfe3ea 45%, #c9c4c0 70%, #e6e6ea 100%); }
  .photo--trainer { left: 800px; width: 400px; background: linear-gradient(100deg, #b9a9ae 0%, #4c4f5a 35%, #eeeeee 60%, #e8c9bc 100%); }
</style>
</head>
<body>
<main class="flyer">
  <section class="column column--employer"></section>
  <section class="column column--analysis"></section>
  <section class="column column--programs"></section>

  <div class="title-band"></div>
  <h2 class="section-title section-title--employer">Ihre Vorteile als<br>Arbeitgeber</h2>
  <h2 class="section-title section-title--analysis">Messung &amp;<br>Analysen</h2>
  <h2 class="section-title section-title--programs">Bewegungs-<br>programme</h2>

  <div class="employer-text">
    <p class="tight">Die betriebliche Gesundheitsförderung hat das Ziel die Gesundheit der Mitarbeiter zu erhalten und zu fördern sowie die Leistungsfähigkeit und Motivation der Belegschaft zu steigern.</p>
    <p>Immer mehr gewinnen jedoch folgende Punkte an Bedeutung für Unternehmen:</p>
    <p style="line-height:19.5px"><strong>1) Mitarbeiterbindung &amp;<br>2) Arbeitgeber Attraktivität zu erhöhen, um ein Vorteil am Bewerbermarkt zu erzielen.</strong></p>
    <p>Auch da können wir Sie mit unserem Know-how und abgerundeten Konzept unterstützen.</p>
    <p>In regelmäßigen Abständen setzen wir uns mit Ihren Mitarbeitern in Verbindung und erfragen den jeweiligen IST Stand und besprechen gemeinsames Vorgehen, um gesundheitliche Problematiken im Handlungsfeld Bewegung und Entspannung präventiv vorzubeugen.</p>
    <p>Ihre Mitarbeiter werden dadurch in festen monatlichen Intervallen sensibilisiert dass Sie sich um das Wohlbefinden Ihrer Mitarbeiter kümmern und Sie auch darin investieren.</p>
    <p>Sie als Arbeitgeber können nicht wissen und auch zeitlich nicht gewährleisten welche individuellen gesundheitlichen Problematiken Ihre Mitarbeiter haben. Deshalb bieten wir Ihnen eine individuelle Lösung an Dienstleistung, welche den individuellen Bedarf Ihrer Mitarbeiter deckt.</p>
    <p>Einen Auszug aus unseren Leistungen damit Sie eine Vorstellung bekommen was wir Ihnen und Ihren Mitarbeitern bieten können.</p>
  </div>

  <div class="analysis-text">
    <p>Messung &amp; Analysen zur individuellen Stress- und Resilienzdiagnostik um zielorientiert ein Streßmanagment in Ihrem Betrieb zu implementieren.</p>
    <p>Dokumentation von Körperdaten und Risikofaktoren in einer Eingangskontrolle und einem ½ jährlichen Wiederholung der Kontrolle.</p>
    <p class="gap">Wirbelsäulen- und Haltungsscreenings, Haltung, Beweglichkeit und Haltungskomponenten werden anschaulich dargestellt und bilden die Basis für zielführende Visualisierung und fundierte Übungsempfehlung.</p>
    <p class="gap">Analysen von Körperstabilität und Gleichgewicht; StabiScan Pro ist ein erprobtes Analysetool für das Thema Körperstabilität</p>
  </div>

  <div class="program-box"></div>
  <div class="program" style="left:809px;top:231px"><div class="program__number">1</div><div class="program__label" style="top:57px">Entspannungskurse<br>Hatha Yoga</div></div>
  <div class="program" style="left:996px;top:231px"><div class="program__number">4</div><div class="program__label" style="top:57px;left:-10px;width:200px">Ganzkörper Training an Geräten</div></div>
  <div class="program" style="left:809px;top:344px"><div class="program__number">2</div><div class="program__label" style="top:60px">Pilates</div></div>
  <div class="program" style="left:996px;top:344px"><div class="program__number">5</div><div class="program__label" style="top:60px">Fit am Arbeitsplatz</div></div>
  <div class="program" style="left:809px;top:464px"><div class="program__number">3</div><div class="program__label" style="top:58px">Rückengymnastik</div></div>
  <div class="program" style="left:996px;top:464px"><div class="program__number">6</div><div class="program__label" style="top:58px;left:-10px;width:200px">Online-Präventionskurs (zeitlich und räumlich unabhängig)</div></div>

  <div class="photo photo--group-class" role="img" aria-label="Foto: Trainerin betreut eine Gruppe beim Gerätetraining im hellen Kursraum"></div>
  <div class="photo photo--trainer" role="img" aria-label="Foto: Trainerin im weißen Kittel neben einer Teilnehmerin an Trainingsgeräten"></div>
</main>
</body>
</html>
```